Business Card Project for Firm Deck Hoisting

Business name is "Firm Deck Hoisting" we are a scaffolding & rigging business specialising in local and remote work for:
- scaffolding (residential, commercial, industrial)
- rigging
-man material hoists
- swing stages
- labour hire

On the back of the card I would like FDH as the symbol / logo. I have attached the logos we have had created by sketch harbour. We would like to use bold colours – preferably as the same colour scheme as the logo.

Target Market(s)

Construction business

Industry/Entity Type

Construction

Contact Information for Business Card

name: Owen Pellew
Title: Director
Phone: 0491 572 864
Address: PO BOX 3251, Merrowfield SA 5199
Email: owen@firmdeckhoisting.com.au
Website: www.firmdeckhoisting.com.au

Font styles to use
Sans Serif

Requirements
Must have
• Must use existing logo & prefering using bold colours
Nice to have
• Would be nice to have a line of dot points in what we specialise in but not essential
• Would be nice to see some designs with a slogan but not essential
Should not have
• NA

```html
<!DOCTYPE html>
<html lang="en">
<head>
<meta charset="utf-8">
<title>Firm Deck Hoisting – Business Card</title>
<link rel="stylesheet" href="https://fonts.googleapis.com/css2?family=Montserrat:wght@400;500;700;800&family=Michroma&display=swap">
<style>
  :root {
    --brand-blue: #1177c2;
    --ink: #050505;
    --paper: #ffffff;
    --stage: #2b2b2d;
    --muted: #e9e9e9;
  }
  * { box-sizing: border-box; margin: 0; padding: 0; }
  html, body { width: 1200px; height: 900px; overflow: hidden; }
  body {
    background: var(--stage);
    font-family: "Montserrat", Arial, sans-serif;
    position: relative;
  }
  .card {
    position: absolute;
    width: 560px;
    height: 320px;
    border-radius: 24px;
    overflow: hidden;
    box-shadow: 0 14px 30px rgba(0,0,0,.45);
  }

  /* Front: services */
  .card-front { left: 70px; top: 100px; background: var(--brand-blue); }
  .front-wordmark {
    position: absolute;
    left: 190px; top: 58px;
    font-weight: 800;
    font-size: 112px;
    letter-spacing: 2px;
    line-height: 1;
    color: var(--ink);
  }
  .service-list {
    position: absolute;
    left: 92px; top: 196px;
    list-style: none;
    color: var(--paper);
    font-size: 15px;
    font-weight: 500;
    line-height: 1.35;
  }
  .service-list li::before { content: "-- "; }

  /* Back: contact */
  .card-back { left: 570px; top: 480px; background: var(--ink); }
  .brand-strip {
    position: absolute;
    left: 0; top: 0; bottom: 0;
    width: 150px;
    background: var(--paper);
    border-right: 5px solid var(--brand-blue);
  }
  .strip-wordmark {
    position: absolute;
    left: 75px; top: 160px;
    transform: translate(-50%, -50%) rotate(-90deg);
    white-space: nowrap;
    font-weight: 800;
    font-size: 26px;
    letter-spacing: 1px;
    color: var(--ink);
  }
  .edge-tab {
    position: absolute;
    right: 0; top: 18px;
    width: 22px; height: 130px;
    background: var(--brand-blue);
    border-radius: 22px 0 0 22px;
  }
  .contact {
    position: absolute;
    right: 58px; top: 56px;
    text-align: right;
    color: var(--paper);
  }
  .contact-name {
    font-family: "Michroma", "Montserrat", sans-serif;
    color: var(--brand-blue);
    font-size: 20px;
    letter-spacing: 1px;
  }
  .contact-role {
    font-weight: 700;
    font-size: 13px;
    letter-spacing: 1px;
    margin-top: 2px;
  }
  .contact-lines {
    list-style: none;
    margin-top: 12px;
    font-size: 14px;
    line-height: 1.4;
    color: var(--muted);
  }
  .contact-lines .gap { margin-top: 14px; }
  .contact-lines .web span { color: var(--brand-blue); }
  .contact-icons {
    position: absolute;
    right: 30px; top: 128px;
    display: flex;
    flex-direction: column;
    gap: 6px;
  }
  .contact-icons svg { width: 12px; height: 12px; display: block; }
</style>
</head>
<body>

  <section class="card card-front" aria-label="Card front">
    <div class="front-wordmark">FDH</div>
    <ul class="service-list">
      <li>Scaffolding (residential, commercial, industrial)</li>
      <li>Rigging</li>
      <li>Man material hoists</li>
      <li>Swing stages</li>
      <li>Labour hire</li>
    </ul>
  </section>

  <section class="card card-back" aria-label="Card back">
    <div class="brand-strip">
      <div class="strip-wordmark">Firm Deck Hoisting</div>
    </div>
    <div class="edge-tab"></div>

    <div class="contact">
      <div class="contact-name">OWEN PELLEW</div>
      <div class="contact-role">DIRECTOR</div>
      <ul class="contact-lines">
        <li>PO BOX 3251</li>
        <li>Merrowfield SA 5199</li>
        <li>0491 572 864</li>
        <li class="gap">owen@firmdeckhoisting.com.au</li>
        <li class="web">www.<span>firmdeckhoisting</span>.com.au</li>
      </ul>
    </div>

    <div class="contact-icons" aria-hidden="true">
      <svg viewBox="0 0 12 12"><path d="M3 1 L5 3.5 L3.8 5 Q5 7.5 7 8.2 L8.5 7 L11 9 L9.5 11 Q3 10 1 2.5 Z" fill="var(--brand-blue)"/></svg>
      <svg viewBox="0 0 12 12"><rect x="1" y="2.5" width="10" height="7" rx="1" fill="none" stroke="var(--brand-blue)" stroke-width="1.3"/><path d="M1.5 3 L6 6.5 L10.5 3" fill="none" stroke="var(--brand-blue)" stroke-width="1.3"/></svg>
      <svg viewBox="0 0 12 12"><circle cx="6" cy="6" r="4.8" fill="none" stroke="var(--brand-blue)" stroke-width="1.2"/><ellipse cx="6" cy="6" rx="2" ry="4.8" fill="none" stroke="var(--brand-blue)" stroke-width="1"/><line x1="1.2" y1="6" x2="10.8" y2="6" stroke="var(--brand-blue)" stroke-width="1"/></svg>
    </div>
  </section>

</body>
</html>
```